2018 Fundraiser Event Flier

We are a non profit that works in the homeless community, The Lanternbrook Alliance. We offer a unique program of supported employment that is all about community engagement and building relationships not only with our participants but with community businesses and non profit partners. Our mission statement is "We seek and foster partnerships between the business and nonprofit communities to respectfully and effectively guide individuals from disenfranchised communities forward in sustainable employment to realize their potential of fully enriched lives for themselves and their families" We are having a fundraising event on Dec 13 and need a flier to advertise the event both via email and physical postings. We like a black background and bright colors (see uploaded example) and want to advertise the event and a small amount about who we are. Fun and bright. We will upload two of our logos and two photos that we have used in branding previously.

```html
<!DOCTYPE html>
<html lang="en">
<head>
<meta charset="utf-8">
<title>The Lanternbrook Alliance – Charity of the Month Flier</title>
<link rel="stylesheet" href="https://fonts.googleapis.com/css2?family=Patrick+Hand&family=Patrick+Hand+SC&display=swap">
<style>
  :root {
    --page: #e6e3de;
    --ink: #000000;
    --paper: #ffffff;
    --yellow: #fff200;
    --green: #1dbb3a;
    --blue: #05a6e3;
    --pink: #f45ba8;
  }
  html, body {
    margin: 0;
    width: 1200px;
    height: 1200px;
    overflow: hidden;
    background: var(--page);
  }
  .flier {
    position: absolute;
    left: 194px;
    top: 30px;
    width: 812px;
    height: 1140px;
    display: block;
  }
  .caps { font-family: "Patrick Hand SC", "Patrick Hand", cursive; }
  .hand { font-family: "Patrick Hand", cursive; }
  .bg-black { fill: var(--ink); }
  .cloud-yellow { fill: var(--yellow); }
  .cloud-green { fill: var(--green); }
  .cloud-white { fill: var(--paper); }
  .cloud-blue { fill: var(--blue); }
  .cloud-pink { fill: var(--pink); }
  .dot { fill: var(--paper); }
  .t-ink { fill: var(--ink); }
  .t-white { fill: var(--paper); }
  .t-yellow { fill: var(--yellow); }
  .t-green { fill: var(--green); }
  .t-blue { fill: var(--blue); }
  .t-pink { fill: var(--pink); }
  .mission { font-size: 19.5px; }
  .program { font-size: 16.5px; }
  .beer { font-size: 20px; letter-spacing: 1px; }
  .venue { font-size: 23px; letter-spacing: 1.5px; }
  .date { font-size: 38px; letter-spacing: 2px; }
  .tagline { font-size: 24px; letter-spacing: 1px; }
  .quote { font-size: 13.5px; letter-spacing: .5px; }
  .label { font-size: 17px; letter-spacing: 1px; }
  .speaker { font-size: 13px; letter-spacing: 1px; }
  .web { font-size: 22px; letter-spacing: 1.5px; }
  .charity { font-size: 23px; letter-spacing: 1px; }
  .brand-top { font-size: 29px; letter-spacing: 1px; }
  .brand-bottom { font-size: 19px; }
</style>
</head>
<body>
<svg class="flier" viewBox="0 0 826 1160" xmlns="http://www.w3.org/2000/svg">
  <defs>
    <linearGradient id="photoTone" x1="0" y1="0" x2="1" y2="1">
      <stop offset="0" stop-color="#2b2b2b"/>
      <stop offset=".45" stop-color="#a7a7a7"/>
      <stop offset=".75" stop-color="#6d6d6d"/>
      <stop offset="1" stop-color="#2e2e2e"/>
    </linearGradient>
    <path id="arcWhat" d="M625,325 Q720,345 760,440"/>
    <path id="arcWhere" d="M62,565 Q95,470 215,440"/>
    <path id="arcSpeaker" d="M725,878 Q785,900 800,975"/>
  </defs>

  <!-- base -->
  <rect class="bg-black" width="826" height="1160"/>

  <!-- photo area -->
  <rect class="photo" width="826" height="640" fill="url(#photoTone)" role="img" aria-label="Black and white photo of several hands together holding a small cardboard model house"/>

  <!-- black overlays -->
  <path class="bg-black" d="M0,415 C170,420 300,420 380,400 C470,370 560,335 660,328 C720,324 780,328 826,335 L826,1160 L0,1160 Z"/>
  <circle class="bg-black" cx="138" cy="120" r="168"/>
  <circle class="bg-black" cx="318" cy="172" r="80"/>
  <circle class="dot" cx="796" cy="280" r="11"/>
  <circle class="dot" cx="745" cy="273" r="5"/>
  <circle class="dot" cx="715" cy="300" r="11"/>
  <circle class="dot" cx="96" cy="458" r="11"/>
  <circle class="dot" cx="133" cy="412" r="5"/>
  <circle class="dot" cx="338" cy="467" r="10"/>
  <circle class="dot" cx="822" cy="340" r="14"/>

  <!-- brand top -->
  <circle class="dot" cx="135" cy="112" r="38"/>
  <text class="caps t-white brand-top" x="135" y="185" text-anchor="middle">The Lanternbrook</text>
  <text class="caps t-white brand-top" x="135" y="215" text-anchor="middle">Alliance</text>

  <text class="caps t-yellow charity" text-anchor="middle">
    <tspan x="313" y="157">CHARITY</tspan>
    <tspan x="313" y="185">OF THE</tspan>
    <tspan x="313" y="213">MONTH</tspan>
  </text>

  <!-- blue cloud: venue -->
  <g class="cloud-blue">
    <circle cx="180" cy="835" r="85"/>
    <circle cx="290" cy="820" r="80"/>
    <circle cx="390" cy="850" r="75"/>
    <circle cx="200" cy="900" r="60"/>
    <circle cx="300" cy="900" r="65"/>
    <circle cx="400" cy="905" r="55"/>
    <circle cx="150" cy="880" r="50"/>
  </g>

  <!-- white cloud: beer -->
  <g class="cloud-white">
    <circle cx="450" cy="705" r="72"/>
    <circle cx="560" cy="700" r="70"/>
    <circle cx="660" cy="735" r="68"/>
    <circle cx="440" cy="780" r="70"/>
    <circle cx="545" cy="785" r="85"/>
    <circle cx="650" cy="810" r="55"/>
  </g>

  <!-- yellow cloud: mission -->
  <g class="cloud-yellow">
    <circle cx="565" cy="410" r="80"/>
    <circle cx="480" cy="465" r="78"/>
    <circle cx="640" cy="450" r="72"/>
    <circle cx="680" cy="510" r="72"/>
    <circle cx="460" cy="545" r="70"/>
    <circle cx="565" cy="540" r="90"/>
    <circle cx="660" cy="575" r="62"/>
    <ellipse cx="563" cy="600" rx="125" ry="45"/>
  </g>
  <text class="hand t-ink mission" text-anchor="middle">
    <tspan x="563" y="376">"We</tspan>
    <tspan x="563" y="398">seek and foster</tspan>
    <tspan x="563" y="421">partnerships between</tspan>
    <tspan x="563" y="443">the business and nonprofit</tspan>
    <tspan x="563" y="466">communities to respectfully</tspan>
    <tspan x="563" y="488">and effectively guide individuals</tspan>
    <tspan x="563" y="511">from disenfranchised</tspan>
    <tspan x="563" y="533">communities forward in</tspan>
    <tspan x="563" y="556">sustainable employment to</tspan>
    <tspan x="563" y="578">realize their potential of fully</tspan>
    <tspan x="563" y="601">enriched lives for themselves</tspan>
    <tspan x="563" y="623">and their families"</tspan>
  </text>
  <text class="caps t-yellow label"><textPath href="#arcWhat">WHAT DO WE DO ?</textPath></text>

  <text class="caps t-ink beer" text-anchor="middle">
    <tspan x="545" y="690">ENJOY A BEER</tspan>
    <tspan x="545" y="714">AT COPPERLEAF IN THE</tspan>
    <tspan x="545" y="738">MONTH OF DECEMBER</tspan>
    <tspan x="545" y="762">AND 1% OF ALL SALES</tspan>
    <tspan x="545" y="786">SUPPORTS</tspan>
    <tspan x="545" y="810">THE LANTERNBROOK</tspan>
    <tspan x="545" y="834">ALLIANCE</tspan>
  </text>

  <!-- green cloud: program -->
  <g class="cloud-green">
    <circle cx="240" cy="540" r="95"/>
    <circle cx="145" cy="600" r="80"/>
    <circle cx="335" cy="580" r="82"/>
    <circle cx="120" cy="690" r="65"/>
    <circle cx="230" cy="660" r="100"/>
    <circle cx="350" cy="690" r="68"/>
    <circle cx="260" cy="730" r="55"/>
    <circle cx="355" cy="635" r="68"/>
  </g>
  <text class="hand t-ink program" text-anchor="middle">
    <tspan x="242" y="517">TLA provides this</tspan>
    <tspan x="242" y="536">support through the</tspan>
    <tspan x="242" y="555">placement of Peer</tspan>
    <tspan x="242" y="574">Mentor/Trainers in the</tspan>
    <tspan x="242" y="593">workforce creating a safe and</tspan>
    <tspan x="242" y="612">dynamic training workspace within</tspan>
    <tspan x="242" y="631">the business operations of our</tspan>
    <tspan x="242" y="650">Community Partners:</tspan>
    <tspan x="252" y="682">– Harborline Service Partners</tspan>
    <tspan x="252" y="701">/ Ridgefield Zoo</tspan>
    <tspan x="252" y="728">– Kestrel Grand Hotel /</tspan>
    <tspan x="252" y="747">Willow Bend</tspan>
  </text>
  <text class="caps t-green label"><textPath href="#arcWhere">WHERE DO WE DO IT ?</textPath></text>

  <!-- venue text -->
  <text class="caps t-white venue" text-anchor="middle">
    <tspan x="245" y="810">COPPERLEAF BREWING CO,</tspan>
    <tspan x="245" y="838">418 MAPLE AVENUE,</tspan>
    <tspan x="245" y="865">ASHFORD CO 80999</tspan>
  </text>
  <text class="caps t-yellow date" x="286" y="915" text-anchor="middle">DECEMBER 13</text>

  <!-- taglines -->
  <text class="caps t-white tagline" text-anchor="middle">
    <tspan x="110" y="972">ENJOY</tspan>
    <tspan x="110" y="1004">GREAT</tspan>
  </text>
  <text class="caps t-yellow tagline" text-anchor="middle">
    <tspan x="260" y="1003">DISCOVER NEW</tspan>
    <tspan x="260" y="1034">FRIENDS</tspan>
  </text>
  <text class="caps t-blue tagline" text-anchor="middle">
    <tspan x="472" y="982">SUPPORT YOUR</tspan>
    <tspan x="472" y="1013">COMMUNITY</tspan>
  </text>

  <!-- pink cloud: quote -->
  <g class="cloud-pink">
    <circle cx="640" cy="955" r="52"/>
    <circle cx="712" cy="960" r="50"/>
    <circle cx="610" cy="1010" r="48"/>
    <circle cx="680" cy="1010" r="62"/>
    <circle cx="745" cy="1010" r="45"/>
  </g>
  <text class="caps t-white quote" text-anchor="middle">
    <tspan x="675" y="928">LIKE SLAVERY</tspan>
    <tspan x="675" y="945">AND APARTHEID,</tspan>
    <tspan x="675" y="962">POVERTY IS NOT</tspan>
    <tspan x="675" y="980">NATURAL. IT IS MAN-MADE</tspan>
    <tspan x="675" y="997">AND IT CAN BE OVERCOME</tspan>
    <tspan x="675" y="1014">AND ERADICATED BY THE</tspan>
    <tspan x="675" y="1032">ACTIONS OF HUMAN</tspan>
    <tspan x="675" y="1049">BEINGS.</tspan>
  </text>
  <text class="caps t-pink speaker"><textPath href="#arcSpeaker">AMARA OKAFOR</textPath></text>

  <!-- footer -->
  <text class="caps t-yellow brand-bottom">
    <tspan x="33" y="1092">The Lanternbrook</tspan>
    <tspan x="33" y="1114">Alliance</tspan>
  </text>
  <text class="caps t-white web" x="200" y="1110">WWW.LANTERNBROOKALLIANCE.ORG</text>
</svg>
</body>
</html>
```